UX - Need some screens design for a Skill Assessment Application

I am building an app to carry out skill assessments. Depending on how the assessment is configured, it may have one or more parts
1. Question based assessment (Multiple Choice, True False, Fill in the blanks"
2. Endorsement by two colleagues - A screen that allows user to pick colleagues based on search and shows the status of pending requests
3. A written submission - a page that explains the format of the submission and a file upload
As each assessment can be configured with or without any of the steps, the assessment UI must be such that these areas get hidden/displayed based on configuration.
Colour codes to be used can be #0e78bb and #ffffff
There will also be a start screen (instructions) and an end screen (results)
Target Market(s)
Enterprise software
Number of Pages Required
4 page

```html
<!DOCTYPE html>
<html lang="en">
<head>
<meta charset="utf-8">
<title>UI/UX Designer Assessment – Endorsement</title>
<link href="https://fonts.googleapis.com/css2?family=Inter:wght@400;500;600;700&display=swap" rel="stylesheet">
<style>
:root{
  --brand:#0e78bb;
  --nav:#0b5aa6;
  --teal:#1a928f;
  --ink:#1f2328;
  --muted:#4b5563;
  --soft:#9aa3ad;
  --line:#d9dde3;
  --band:#e9f0f7;
  --note:#f3f4f6;
  --white:#ffffff;
}
*{box-sizing:border-box;margin:0;padding:0}
html,body{width:1200px;height:771px;overflow:hidden;background:var(--white)}
body{font-family:"Inter",sans-serif;color:var(--ink)}
.page{width:1400px;height:900px;position:relative;transform:scale(.857143);transform-origin:0 0}
.abs{position:absolute}
.topbar{left:0;top:0;width:1400px;height:51px;background:var(--nav)}
.brand{left:82px;top:14px;display:flex;align-items:center;gap:12px;color:var(--white);font-weight:600;font-size:16px}
.brand-dot{width:24px;height:24px;border-radius:50%;background:#5cc3ef}
.nav{left:569px;top:0;display:flex;gap:24px;height:51px}
.nav a{color:#cfe0f2;font-size:14px;text-decoration:none;line-height:54px;position:relative}
.nav a.active{color:var(--white);font-weight:600}
.nav a.active::after{content:"";position:absolute;left:0;right:0;bottom:0;height:3px;background:#35b6ee}
.top-icons{right:82px;top:10px;display:flex;gap:18px;align-items:center}
.avatar-me{width:32px;height:32px;border-radius:50%;background:linear-gradient(135deg,#3a3f55,#c9a394)}
.crumbs{left:66px;top:76px;display:flex;align-items:center;gap:8px;font-size:13px;color:var(--muted)}
.crumbs a{color:var(--brand);text-decoration:none;margin-left:7px}
.title{left:103px;top:116px;display:flex;align-items:center;gap:14px;font-size:24px;font-weight:600}
.score{right:103px;top:114px;font-size:32px;font-weight:700}
.score small{font-size:16px}
.teal{left:0;top:165px;width:1400px;height:7px;background:var(--teal)}
.band{left:0;top:172px;width:1400px;height:53px;background:var(--band);border-bottom:1px solid var(--line);font-size:12px;display:flex;align-items:center;padding:0 103px}
.band .item{padding-right:24px;margin-right:24px;border-right:1px solid #c6ced8}
.band .item:nth-child(3){border:0}
.band b{font-weight:400;color:var(--brand)}
.band .grey{color:var(--muted)}
.band .updated{margin-left:auto;font-size:13px;color:var(--muted)}
.band .updated span{color:var(--ink)}
.steps{left:96px;top:296px}
.step{display:flex;align-items:center;gap:16px;font-size:16px;height:22px}
.step.done{color:var(--brand)}
.step-rail{width:1px;height:31px;background:var(--line);margin-left:7.5px}
.dot{width:16px;height:16px;border-radius:50%;border:1px solid #c9ced6;background:var(--white)}
.section-head{left:427px;top:254px;width:870px;height:44px;border-bottom:1px solid var(--line);display:flex;justify-content:space-between}
.section-head h2{font-size:18px;font-weight:600}
.save{color:var(--brand);font-size:13px;display:flex;gap:10px;align-items:flex-start;padding-top:4px}
.control{top:318px;height:36px;border:1px solid var(--line);border-radius:3px;font-size:13px;display:flex;align-items:center;justify-content:space-between;padding:0 15px}
.rows{left:427px;top:370px;width:546px}
.row{height:48px;border:1px solid var(--line);border-radius:3px;margin-bottom:4px;display:flex;align-items:center;padding:0 7px}
.check{width:15px;height:15px;border:1px solid #cfd4da;border-radius:2px;margin-right:9px}
.row.disabled .check{background:#eef0f2}
.pic{width:32px;height:32px;border-radius:50%;margin-right:12px}
.name{font-size:14px;font-weight:500;flex:1}
.role{font-size:12px;color:var(--muted);margin-right:54px}
.btn{font-family:inherit;font-size:13px;border-radius:3px;border:1px solid var(--brand);background:var(--brand);color:var(--white);height:27px;padding:0 11px}
.btn.ghost{background:var(--white);color:var(--brand)}
.row .btn{width:49px;padding:0;position:absolute;right:7px}
.row .btn.ghost{width:67px}
.row{position:relative}
.row.disabled .role{margin-right:72px}
.pager{left:560px;top:754px;display:flex;align-items:center;gap:16px;font-size:13px}
.pg{height:36px;border-radius:3px;display:flex;align-items:center;justify-content:center;gap:6px}
.note{left:1047px;top:318px;width:250px;height:198px;background:var(--note);border-radius:4px;padding:22px 24px}
.note h3{font-size:18px;font-weight:500;margin-bottom:14px}
.note p{font-size:14px;line-height:24px;color:var(--muted)}
.footer{left:0;top:827px;width:1400px;height:1px;background:var(--line)}
.foot-btn{top:844px;height:36px;font-size:13px}
</style>
</head>
<body>
<div class="page">
  <header class="abs topbar"></header>
  <div class="abs brand"><span class="brand-dot"></span>Skillmark</div>
  <nav class="abs nav"><a class="active" href="#">Assessments</a><a href="#">Colleagues</a><a href="#">Results</a></nav>
  <div class="abs top-icons">
    <svg width="20" height="20" viewBox="0 0 24 24" fill="none" stroke="#fff" stroke-width="1.6"><path d="M6 16V11a6 6 0 0 1 12 0v5l2 2H4z"/><path d="M10 20a2 2 0 0 0 4 0"/></svg>
    <svg width="20" height="20" viewBox="0 0 24 24" fill="none" stroke="#fff" stroke-width="1.6"><circle cx="12" cy="12" r="3"/><path d="M12 2l2 3 3.5-.5.5 3.5 3 2-2 3 .5 3.5-3.5.5-2 3-2-3-3.5-.5.5-3.5-3-2 3-2-.5-3.5L10 5z"/></svg>
    <div class="avatar-me" role="img" aria-label="User profile photo"></div>
  </div>

  <div class="abs crumbs">
    <svg width="22" height="22" viewBox="0 0 24 24" fill="none" stroke="#0e78bb" stroke-width="1.8"><circle cx="12" cy="12" r="10"/><path d="M13 8l-4 4 4 4M9 12h7"/></svg>
    <a href="#">Assessment</a> / <span>Application Design Capabilities</span>
  </div>
  <div class="abs title">
    <svg width="26" height="26" viewBox="0 0 24 24" fill="none" stroke="#4b5563" stroke-width="1.5"><path d="M15 2H4v20h8"/><path d="M7 7h5M7 11h5M7 15h3"/><circle cx="17" cy="17" r="4"/><path d="M15.3 17l1.2 1.2 2.2-2.3"/></svg>
    <h1 style="font-size:24px;font-weight:600">UI/UX Designer Assessment</h1>
  </div>
  <div class="abs score">100<small>%</small></div>
  <div class="abs teal"></div>
  <div class="abs band">
    <div class="item">Assessment Date: <b>Feb 12, 2024</b></div>
    <div class="item">Assessment Type: <b>UI/UX Skill</b></div>
    <div class="item">Due Date: <span class="grey">17/02/2024</span></div>
    <div class="updated">Last Updated: <span>23/05/2024</span></div>
  </div>

  <div class="abs steps">
    <div class="step done"><svg width="16" height="16" viewBox="0 0 16 16"><circle cx="8" cy="8" r="8" fill="#1a928f"/><path d="M4.5 8.2l2.3 2.2 4.5-4.6" stroke="#fff" stroke-width="1.6" fill="none"/></svg>Quiz</div>
    <div class="step-rail"></div>
    <div class="step"><span class="dot"></span>Endorsement</div>
  </div>

  <div class="abs section-head">
    <h2>Endorsement</h2>
    <div class="save"><svg width="18" height="18" viewBox="0 0 24 24" fill="none" stroke="#0e78bb" stroke-width="1.8"><path d="M4 4h13l3 3v13H4z"/><path d="M8 4v5h7V4M8 20v-6h8v6"/></svg>Save Progress</div>
  </div>

  <div class="abs control" style="left:427px;width:232px">All categories<svg width="12" height="12" viewBox="0 0 12 12"><path d="M2 4l4 4 4-4" stroke="#1f2328" stroke-width="1.4" fill="none"/></svg></div>
  <div class="abs control" style="left:667px;width:182px;color:var(--soft)">Search<svg width="18" height="18" viewBox="0 0 24 24" fill="none" stroke="#6b7280" stroke-width="1.8"><circle cx="11" cy="11" r="7"/><path d="M16 16l5 5"/></svg></div>
  <div class="abs control" style="left:857px;width:116px;color:var(--soft);justify-content:center">Send Request</div>

  <div class="abs rows">
    <div class="row"><span class="check"></span><span class="pic" role="img" aria-label="Colleague photo" style="background:#8a6a4a"></span><span class="name">Mei Lin Tao</span><span class="role">Application Design Capabilities</span><button class="btn">Add</button></div>
    <div class="row"><span class="check"></span><span class="pic" role="img" aria-label="Colleague photo" style="background:#3c3f44"></span><span class="name">Harold Dunmore</span><span class="role">UI/UX Designer</span><button class="btn">Add</button></div>
    <div class="row"><span class="check"></span><span class="pic" role="img" aria-label="Colleague photo" style="background:#6d6864"></span><span class="name">Milo Trenton</span><span class="role">Front-end Developer</span><button class="btn">Add</button></div>
    <div class="row"><span class="check"></span><span class="pic" role="img" aria-label="Colleague photo" style="background:#e4b98c"></span><span class="name">Alina Kestrel</span><span class="role">Cybersecurity Analyst</span><button class="btn">Add</button></div>
    <div class="row disabled"><span class="check"></span><span class="pic" role="img" aria-label="Colleague photo" style="background:#9b8880"></span><span class="name">Roland Clayfield</span><span class="role">DevOps Engineer</span><button class="btn ghost">Cancel</button></div>
    <div class="row"><span class="check"></span><span class="pic" role="img" aria-label="Colleague photo" style="background:#6b5a3e"></span><span class="name">Renata Dulwich</span><span class="role">DevOps Engineer</span><button class="btn">Add</button></div>
    <div class="row"><span class="check"></span><span class="pic" role="img" aria-label="Colleague photo" style="background:#7fa8c4"></span><span class="name">Jasper Morrow</span><span class="role">DevOps Engineer</span><button class="btn">Add</button></div>
  </div>

  <div class="abs pager">
    <div class="pg" style="width:96px;border:1px solid var(--line);color:#c3c8cf">‹ Previous</div>
    <div class="pg" style="width:38px;background:var(--brand);color:#fff;font-size:15px">1</div>
    <div style="font-size:15px;color:var(--muted)">2</div>
    <div class="pg" style="width:74px;background:var(--brand);color:#fff;margin-left:12px">Next ›</div>
  </div>

  <aside class="abs note">
    <h3>Note</h3>
    <p>Lorem ipsum dolor sit amet, consecteteur adispiscing elit. Lorem ipsum dolor sit amet, consecteteur adispiscing elit.Lorem ipsum dolor.</p>
  </aside>

  <div class="abs footer"></div>
  <button class="abs btn ghost foot-btn" style="left:103px;width:84px">Go Back</button>
  <button class="abs btn foot-btn" style="left:1142px;width:155px">Submit Assessment</button>
</div>
</body>
</html>
```